" Prospectamos pequenas e médias empresas que necessitam de uma presença na internet para melhorar seus resultados, e oferecemos as melhores soluções para cada negócio. Criamos desde landing pages básicas, até grandes sites com gerenciamento de conteúdo. Otimização para mecanismos de busca, gestão de campanhas de links patrocinados, gestão de blogs e redes sociais, sistemas personalizados, infra estrutura de TI. "

```html
<!DOCTYPE html>
<html lang="pt-BR">
<head>
<meta charset="utf-8">
<title>Vertix Digital — Flyer</title>
<link rel="stylesheet" href="https://fonts.googleapis.com/css2?family=Oswald:wght@500;700&family=Roboto+Condensed:wght@400;700&display=swap">
<style>
  :root{
    --navy:#17275c;
    --navy-deep:#0d1838;
    --orange:#e8531f;
    --white:#ffffff;
    --paper-bg:#e6e6e6;
    --ink:#1c2340;
  }
  *{box-sizing:border-box;margin:0;padding:0}
  html,body{width:1200px;height:1200px;overflow:hidden;background:var(--paper-bg)}
  .flyer{
    position:absolute;left:220px;top:62px;width:760px;height:1076px;
    background:var(--white);overflow:hidden;
    box-shadow:0 8px 30px rgba(0,0,0,.18);
    font-family:"Roboto Condensed",sans-serif;
  }
  .brand{
    position:absolute;left:0;right:0;top:70px;
    display:flex;align-items:center;justify-content:center;gap:18px;
  }
  .brand-dot{width:62px;height:62px;border-radius:50%;background:var(--orange)}
  .brand-name{
    font-family:"Oswald",sans-serif;font-weight:700;font-size:64px;
    color:var(--navy);letter-spacing:1px;line-height:1;
  }
  .hero{
    position:absolute;left:0;top:230px;width:760px;height:560px;
    background:radial-gradient(ellipse at 55% 35%,#5a7fb8 0%,#27407a 35%,var(--navy) 65%,var(--navy-deep) 100%);
  }
  .swoosh{position:absolute;left:0;width:760px}
  .swoosh-top{top:170px;height:150px}
  .swoosh-bottom{top:700px;height:170px}
  .intro{
    position:absolute;right:48px;top:330px;width:240px;
    color:var(--white);font-size:17px;line-height:1.35;
  }
  .headline{
    position:absolute;left:48px;top:570px;
    font-family:"Oswald",sans-serif;font-weight:700;color:var(--white);
    font-size:54px;line-height:1.08;text-transform:uppercase;
  }
  .headline .accent{color:var(--orange)}
  .contact{
    position:absolute;left:0;right:0;top:900px;text-align:center;color:var(--ink);
  }
  .tagline{font-size:30px;font-weight:700}
  .tagline .accent{color:var(--orange)}
  .tagline .strong{color:var(--navy);font-family:"Oswald",sans-serif;font-weight:700}
  .contact-list{
    display:flex;justify-content:center;gap:30px;margin-top:22px;
    font-size:22px;font-weight:700;color:var(--navy);
  }
  .contact-item{display:flex;align-items:center;gap:8px}
  .contact-item svg{width:24px;height:24px}
</style>
</head>
<body>
<article class="flyer">
  <div class="brand">
    <span class="brand-dot"></span>
    <span class="brand-name">Vertix Digital</span>
  </div>

  <div class="hero" role="img" aria-label="Foto de um homem de negócios diante de um mapa-mundi com rede de conexões e perfis"></div>

  <svg class="swoosh swoosh-top" viewBox="0 0 760 150" preserveAspectRatio="none">
    <path d="M0 60 C250 150 520 20 760 70 L760 0 L0 0 Z" fill="var(--white)"/>
    <path d="M0 60 C250 150 520 20 760 70 L760 84 C520 36 250 166 0 78 Z" fill="var(--orange)"/>
    <path d="M0 78 C250 166 520 36 760 84 L760 98 C520 52 250 180 0 94 Z" fill="var(--navy)"/>
  </svg>

  <p class="intro">Se a sua empresa ainda não está na internet, fale com a Vertix Digital e conquiste mais clientes com presença digital.</p>

  <h1 class="headline">O teu negócio<br>realmente está<br>na <span class="accent">internet?</span></h1>

  <svg class="swoosh swoosh-bottom" viewBox="0 0 760 170" preserveAspectRatio="none">
    <path d="M0 110 C260 40 520 150 760 60 L760 170 L0 170 Z" fill="var(--orange)"/>
    <path d="M0 126 C260 58 520 166 760 78 L760 170 L0 170 Z" fill="var(--navy)"/>
    <path d="M0 142 C260 78 520 182 760 96 L760 170 L0 170 Z" fill="var(--white)"/>
  </svg>

  <footer class="contact">
    <p class="tagline"><span class="accent">Estamos</span> <span class="strong">SUPER AFIM</span> de lhe ajudar, <span class="accent">fale conosco</span></p>
    <div class="contact-list">
      <span class="contact-item">
        <svg viewBox="0 0 24 24"><circle cx="12" cy="12" r="11" fill="var(--navy)"/></svg>
        (11) 4021-3300
      </span>
      <span class="contact-item">
        <svg viewBox="0 0 24 24"><path d="M6.6 10.8a15 15 0 0 0 6.6 6.6l2.2-2.2a1 1 0 0 1 1-.25 11.4 11.4 0 0 0 3.6.57 1 1 0 0 1 1 1V20a1 1 0 0 1-1 1A17 17 0 0 1 3 4a1 1 0 0 1 1-1h3.5a1 1 0 0 1 1 1c0 1.25.2 2.45.57 3.57a1 1 0 0 1-.25 1z" fill="var(--navy)"/></svg>
        (11) 4021-3311
      </span>
      <span class="contact-item">
        <svg viewBox="0 0 24 24"><path d="M5 3l14 8-6 1.5L10 19z" fill="var(--navy)"/></svg>
        www.vertixdigital.com.br
      </span>
    </div>
  </footer>
</article>
</body>
</html>
```